Corvael Channel Partner Program Brochure

We need a full color brochure designed for our Channel Partner program. The program is intended to recruit agents to sell our services. There's a lot of information to be communicated and the final design should not look too text heavy.

About Corvael:
Founded in 2007, Corvael is a global BPO/KPO provider delivering superior managed services in the areas of Managed NOC & Network services, App Development, Service Provisioning, Finance & Accounting, Fraud & Security Management, and IP Support to telecommunications companies worldwide. The company consistently helps its clients to dramatically improve their financial performance through its highly specialized services. Corvael is headquartered in the Washington, D.C. area. For more information, visit http://www.corvael-example.com. Follow the company on Twitter @Corvael.

Target Market(s)

Agents in the U.S. selling telecom products and services.

Industry/Entity Type

Telecommunications

Requirements
Must have
• Brochure is a half fold and the template is attached. Good use of balance between imagery/graphic and text.

```html
<!DOCTYPE html>
<html lang="en">
<head>
<meta charset="utf-8">
<title>Corvael Channel Partner Program</title>
<link href="https://fonts.googleapis.com/css2?family=Lato:wght@300;400;700&family=Open+Sans:wght@400;600&display=swap" rel="stylesheet">
<style>
  :root{
    --red:#c0161d;
    --ink:#231f20;
    --text:#3a3a3a;
    --white:#ffffff;
    --rule:#4a4647;
  }
  *{margin:0;padding:0;box-sizing:border-box}
  html,body{width:1200px;height:848px;overflow:hidden;background:var(--white)}
  .brochure{position:relative;width:1200px;height:848px;background:var(--white);font-family:"Open Sans",Arial,sans-serif;color:var(--text)}
  .block{position:absolute}
  .brand{display:flex;align-items:center;gap:10px;font-family:"Lato",Arial,sans-serif;font-weight:700;font-size:40px;letter-spacing:1px;color:var(--ink)}
  .brand-mark{width:18px;height:18px;background:var(--red)}
  .title-panel{background:var(--red);color:var(--white);font-family:"Lato",Arial,sans-serif;font-weight:300;font-size:24.5px;line-height:34px;padding:58px 0 0 46px;letter-spacing:.3px}
  .section-label{background:var(--ink);color:var(--white);font-family:"Lato",Arial,sans-serif;font-weight:300;font-size:19px;line-height:25px;padding:18px 0 0 22px;letter-spacing:.2px}
  .enrol-text{font-size:14.6px;line-height:17px;color:var(--text)}
  .enrol-text p{margin-bottom:17px}
  .enrol-text ol{list-style:none}
  .photo{position:absolute}
  .contact-band{background:var(--ink);color:var(--white);font-family:"Lato",Arial,sans-serif;font-weight:300;font-size:14.5px;display:flex;align-items:center;padding-left:33px;gap:14px}
  .find-out{background:var(--ink);color:var(--white);font-family:"Lato",Arial,sans-serif;font-weight:300;padding:45px 24px 0 20px}
  .find-out h2{font-weight:300;font-size:21px;letter-spacing:.3px;margin-bottom:14px}
  .find-out .row{font-size:14px;padding:8px 0 7px;border-bottom:1px solid var(--rule)}
  .find-out .row:last-child{border-bottom:none}
  .find-out .row span{display:inline-block;width:48px}
  .pitch{font-size:14.6px;line-height:17px;text-align:justify;color:var(--text)}
</style>
</head>
<body>
<div class="brochure">
  <!-- Left page header -->
  <div class="block brand" style="left:38px;top:80px;height:50px"><span class="brand-mark"></span>CORVAEL</div>
  <div class="block title-panel" style="left:297px;top:0;width:302px;height:209px">CORVAEL<br>CHANNEL PARTNER<br>PROGRAM</div>

  <!-- Right page header -->
  <div class="block brand" style="left:613px;top:80px;height:50px"><span class="brand-mark"></span>CORVAEL</div>
  <div class="block title-panel" style="left:897px;top:0;width:303px;height:209px">CORVAEL<br>CHANNEL PARTNER<br>PROGRAM</div>

  <!-- Enrolment -->
  <div class="block section-label" style="left:0;top:206px;width:301px;height:82px">ENROLLING IN THE CORVAEL<br>CHANNEL PARTNER PROGRAM</div>
  <div class="block enrol-text" style="left:48px;top:306px;width:510px">
    <p>Joining the Corvael Channel Partner Program is easy.</p>
    <ol>
      <li>1.&nbsp;&nbsp;Visit www.corvael-example.com/channel-partners</li>
      <li>2.&nbsp;&nbsp;Complete our online application form</li>
      <li>3.&nbsp;&nbsp;Once your application is accepted and you are registered in the program, you will receive a welcome kit and access to sales information</li>
    </ol>
  </div>

  <!-- Photo areas -->
  <div class="photo" role="img" aria-label="Bright data centre with rows of server racks" style="left:594px;top:208px;width:303px;height:210px;background:linear-gradient(160deg,#eef1f4 0%,#c9d0d8 55%,#e6e9ec 100%)"></div>
  <div class="photo" role="img" aria-label="Smiling businesswoman talking on a mobile phone" style="left:897px;top:208px;width:303px;height:210px;background:linear-gradient(110deg,#8fa3b8 0%,#c9b3a3 55%,#e9ecef 100%)"></div>
  <div class="photo" role="img" aria-label="Relaxed businessman leaning back with hands behind his head" style="left:0;top:435px;width:598px;height:352px;background:linear-gradient(135deg,#f4f6f8 0%,#c7d6e6 45%,#dfe6ee 100%)"></div>
  <div class="photo" role="img" aria-label="Businessman in striped tie using a tablet" style="left:598px;top:433px;width:302px;height:210px;background:linear-gradient(150deg,#e9edf1 0%,#c4ccd6 60%,#9ea8b3 100%)"></div>
  <div class="photo" role="img" aria-label="Calculator, coins and financial chart" style="left:900px;top:433px;width:300px;height:210px;background:linear-gradient(135deg,#4d5d70 0%,#8596a8 50%,#c9d3dc 100%)"></div>

  <!-- Left page contact band -->
  <div class="block contact-band" style="left:0;top:787px;width:598px;height:61px">
    <span>+1.888.555.0147</span><span>|</span><span>www.corvael-example.com/channel-partners</span><span>|</span><span>info@corvael-example.com</span>
  </div>

  <!-- Find out more -->
  <div class="block find-out" style="left:600px;top:643px;width:300px;height:205px">
    <h2>FIND OUT MORE</h2>
    <div class="row"><span>Phone</span>+1.888.555.0147</div>
    <div class="row"><span>Online</span>www.corvael-example.com</div>
    <div class="row"><span>E-mail</span>info@corvael-example.com</div>
  </div>

  <div class="block pitch" style="left:918px;top:681px;width:262px">
    The Corvael Partner Program is designed to make your partnership with Corvael highly productive and profitable. When you offer Corvael's best-in-class managed services to telco/cable service providers, you'll boost profitability and grow your business.
  </div>
</div>
</body>
</html>
```